Your conflict - our mediation - joint conflict SOLUTION

With this flyer I am looking for conflict parties who are ready to tackle and resolve their conflict with a prospective mediator. The mediation is free because I am doing it as part of my diploma thesis. Time frame approx. 4 sessions of 2.5 hours each. The wishes and needs of both parties are listened to and “picked out”. In an open, constructive, appreciative framework, solutions are developed and negotiated together.

Target Market(s)

everyone who is ready to deal with himself and his counterpart and everyone who wants to work out a solution with the respect, openness and support of a mediator.

Requirements
Must have
• - "For my diploma thesis I am looking for conflicting parties who are willing to resolve their conflict with a mediator"
- Time frame: 4 x 2.5 hours feasible in Solothurn, Bern, Brugg
- Free of charge
- my coordinates - see business card
- more information at www.lindenhofwerk.ch
Nice to have
• the card should be based on the style of my homepage www.lindenhofwerk.ch and my business card

```html
<!DOCTYPE html>
<html lang="de">
<head>
<meta charset="utf-8">
<title>Lindenhofwerk – Mediation Flyer</title>
<link rel="stylesheet" href="https://fonts.googleapis.com/css2?family=Raleway:wght@400;500;600;700&family=Roboto:wght@400;500&display=swap">
<style>
  :root {
    --plum-dark: #412a52;
    --plum-mid: #7a5f8c;
    --lilac: #a592b8;
    --lilac-icon: #b9a6cc;
    --ink: #222222;
    --white: #ffffff;
    --page-bg: #e4e4e4;
    --gold: #b08d57;
    --green: #2e6b3e;
    --blue: #2f3e8e;
  }
  * { margin: 0; padding: 0; box-sizing: border-box; }
  html, body { width: 1200px; height: 1200px; overflow: hidden; background: var(--page-bg); }
  .flyer {
    position: absolute; left: 190px; top: 20px;
    width: 821px; height: 1161px;
    background: var(--white);
    font-family: "Roboto", Arial, sans-serif;
    color: var(--ink);
    overflow: hidden;
  }
  .top-band { position: absolute; left: 0; top: 0; width: 100%; height: 14px; background: var(--lilac); }

  .brand { position: absolute; left: 77px; top: 90px; display: flex; align-items: center; gap: 14px; }
  .brand-dot { width: 26px; height: 26px; border-radius: 50%; background: var(--plum-mid); }
  .brand-name { font-family: "Raleway", sans-serif; font-weight: 500; font-size: 38px; color: var(--plum-dark); letter-spacing: 0.5px; }

  .intro {
    position: absolute; left: 77px; top: 300px; width: 320px;
    font-family: "Raleway", sans-serif; font-weight: 400;
    font-size: 26px; line-height: 31.5px; color: var(--ink);
  }
  .illustration {
    position: absolute; left: 413px; top: 100px; width: 366px; height: 385px;
    background: linear-gradient(135deg, #c9ad82 0%, #8090c4 50%, #6f9c7a 100%);
    opacity: 0.55; border-radius: 6px;
  }

  .facts {
    position: absolute; left: 0; top: 516px; width: 100%; height: 162px;
    background: var(--plum-dark);
  }
  .fact {
    position: absolute; top: 34px; width: 240px; margin-left: -120px;
    text-align: center; color: var(--white);
  }
  .fact svg { display: block; margin: 0 auto; }
  .fact-label { display: block; margin-top: 16px; font-weight: 500; font-size: 13px; letter-spacing: 0.2px; }

  .conflict {
    position: absolute; left: 0; top: 678px; width: 100%; height: 215px;
    background: var(--plum-mid); color: var(--white); text-align: center;
  }
  .conflict-title { margin-top: 34px; font-family: "Raleway", sans-serif; font-weight: 500; font-size: 27px; word-spacing: 10px; letter-spacing: 0.3px; }
  .conflict-list { width: 600px; margin: 16px auto 0; font-size: 13.5px; line-height: 17px; }
  .conflict-question { margin-top: 22px; font-family: "Raleway", sans-serif; font-weight: 700; font-size: 20px; }

  .mediation { position: absolute; left: 0; top: 893px; width: 100%; height: 181px; text-align: center; }
  .mediation-title { margin-top: 29px; font-family: "Raleway", sans-serif; font-weight: 500; font-size: 27px; letter-spacing: 0.3px; }
  .mediation p { font-size: 13.5px; line-height: 17px; width: 700px; margin: 0 auto; }
  .mediation .lead { margin-top: 10px; }
  .mediation .goal { margin-top: 17px; }

  .bottom-strip { position: absolute; left: 0; top: 1074px; width: 100%; height: 11px; background: var(--lilac); }
  .footer {
    position: absolute; left: 0; top: 1085px; width: 100%; height: 76px;
    background: var(--plum-dark); color: var(--white);
    display: flex; align-items: center; justify-content: center;
    font-family: "Raleway", sans-serif; font-weight: 600; font-size: 21px;
  }
</style>
</head>
<body>
<main class="flyer">
  <div class="top-band"></div>

  <div class="brand">
    <span class="brand-dot"></span>
    <span class="brand-name">Lindenhofwerk</span>
  </div>

  <p class="intro">For my diploma thesis I am looking for conflicting parties who are willing to resolve their conflict with a mediator</p>

  <div class="illustration" role="img" aria-label="Sketched illustration of three people in conversation with a mediator"></div>

  <section class="facts">
    <div class="fact" style="left:164px">
      <svg width="60" height="60" viewBox="0 0 60 60" fill="none" stroke="var(--lilac-icon)" stroke-width="2.5" stroke-linecap="round">
        <circle cx="30" cy="30" r="27"/>
        <circle cx="30" cy="30" r="22"/>
        <path d="M28 16 V31 L36 37"/>
      </svg>
      <span class="fact-label">4 X 2.5 HOURS</span>
    </div>
    <div class="fact" style="left:411px">
      <svg width="60" height="60" viewBox="0 0 60 60" fill="none" stroke="var(--lilac-icon)" stroke-width="2.5" stroke-linejoin="round">
        <path d="M30 58 C20 44 11 34 11 22 A19 19 0 0 1 49 22 C49 34 40 44 30 58 Z"/>
        <circle cx="30" cy="22" r="8"/>
      </svg>
      <span class="fact-label">SOLOTHURN, BERN, BRUGG</span>
    </div>
    <div class="fact" style="left:657px">
      <svg width="60" height="60" viewBox="0 0 60 60" fill="none" stroke="var(--lilac-icon)" stroke-width="2.5">
        <ellipse cx="16" cy="26" rx="11" ry="4"/>
        <path d="M5 26 v20 a11 4 0 0 0 22 0 v-20 M5 33 a11 4 0 0 0 22 0 M5 40 a11 4 0 0 0 22 0"/>
        <ellipse cx="44" cy="10" rx="11" ry="4"/>
        <path d="M33 10 v36 a11 4 0 0 0 22 0 v-36 M33 17 a11 4 0 0 0 22 0 M33 24 a11 4 0 0 0 22 0 M33 31 a11 4 0 0 0 22 0 M33 38 a11 4 0 0 0 22 0"/>
      </svg>
      <span class="fact-label">FREE OF CHARGE</span>
    </div>
  </section>

  <section class="conflict">
    <h2 class="conflict-title">KONFLIKT STREIT BLOCKADE</h2>
    <p class="conflict-list">mit Ihrer Ehefrau … Ihrem Vertragspartner … Ihrer Nachbarin … Ihrem Mieter … Ihrer Tochter … Ihrem Pächter … Ihrer Schwester … Ihrem Geschäftspartner … Ihrer Vorgesetzten … Ihrem Mitarbeiter … Ihrem Vater … Ihrer Vermieterin … Ihrem Freund …</p>
    <p class="conflict-question">Sie kommen nicht mehr weiter?</p>
  </section>

  <section class="mediation">
    <h2 class="mediation-title">MEDIATION</h2>
    <p class="lead">Die Konfliktparteien erarbeiten selber eine Lösung, begleitet und geführt durch eine Mediatorin.</p>
    <p class="goal">Ziel ist eine gemeinsam erarbeitete, stimmige, nachhaltige Lösung, die einen konstruktiven Umgang zwischen den Konfliktparteien wieder möglich macht.</p>
  </section>

  <div class="bottom-strip"></div>
  <footer class="footer">www.lindenhofwerk.ch</footer>
</main>
</body>
</html>
```